Bramwell's Mobile Transport

we would like a new logo for our mobile home transport company we are based in Colorado . what we would like is a mobile home toter ( truck) in a stylish piece of art work Haling a mobile home behind it from a left to right 3-d view, so that you can see the front of the truck and the whole left side of the truck and mobile home, the truck colors are an emerald green and white two-tone the top half the emerald green and the bottom half is to be white, and would like to see something creative with the name of the company as in style please nothing clesha as in with the Irish culture. please see attached examples of truck and truck artwork style.

It Company

00a990

```html
<!DOCTYPE html>
<html lang="en">
<head>
<meta charset="utf-8">
<title>Bramwell's Mobile Transport – Business Card</title>
<link rel="stylesheet" href="https://fonts.googleapis.com/css2?family=Source+Sans+3:wght@400;600;700;900&display=swap">
<style>
  :root {
    --green: #12a032;
    --green-pale: #dfe9e0;
    --white: #ffffff;
    --black: #050505;
    --ink: #0a0a0a;
    --stage: #e9ecea;
    --card-w: 640px;
    --card-h: 380px;
  }
  * { box-sizing: border-box; margin: 0; padding: 0; }
  html, body {
    width: 1200px; height: 914px; overflow: hidden;
    background: var(--stage);
    font-family: "Source Sans 3", "Myriad Pro", sans-serif;
  }
  .canvas { position: relative; width: 1200px; height: 914px; }
  .card {
    position: absolute; left: 280px;
    width: var(--card-w); height: var(--card-h);
    border-radius: 30px; overflow: hidden;
    box-shadow: 0 6px 18px rgba(0,0,0,0.18);
  }
  .card--front { top: 50px; background: var(--green); }
  .card--back { top: 484px; background: var(--white); }

  /* company name: one colour, one weight, with a plain square */
  .company-name {
    position: absolute; display: flex; align-items: flex-start; gap: 12px;
    width: 290px;
    color: var(--ink); font-weight: 700; font-size: 30px; line-height: 1.1;
  }
  .company-name__square {
    flex: none; width: 18px; height: 18px; margin-top: 8px;
    background: var(--green);
  }
  .card--front .company-name { left: 40px; top: 148px; }
  .card--back .company-name { left: 40px; top: 70px; }

  /* front */
  .front-band { position: absolute; inset: 0; width: 100%; height: 100%; }
  .truck-art {
    position: absolute; border-radius: 6px;
    background: linear-gradient(135deg, var(--green) 0%, var(--green-pale) 55%, var(--green) 100%);
  }
  .card--front .truck-art { left: 350px; top: 108px; width: 248px; height: 150px; }
  .web {
    position: absolute; left: 150px; top: 306px;
    color: var(--white); font-weight: 600; font-size: 20px; letter-spacing: 0.6px;
    transform: rotate(6deg); transform-origin: left center;
  }

  /* back */
  .card--back .truck-art { left: 352px; top: 22px; width: 262px; height: 148px; }
  .services-bar {
    position: absolute; left: 0; top: 196px; width: 100%; height: 30px;
    background: var(--green); color: var(--white);
    display: flex; justify-content: flex-end; align-items: center;
    padding-right: 22px; gap: 18px;
    font-weight: 600; font-size: 17px; letter-spacing: 3px;
  }
  .contact-panel {
    position: absolute; left: 0; top: 226px; width: 100%; bottom: 0;
    background: var(--black); color: var(--white);
  }
  .person { position: absolute; left: 46px; top: 14px; font-weight: 600; letter-spacing: 3px; line-height: 1.05; }
  .person__name { display: block; font-size: 19px; }
  .person__role { display: block; font-size: 17px; padding-left: 30px; }
  .contacts { position: absolute; right: 60px; top: 36px; font-size: 14px; font-weight: 600; letter-spacing: 2.5px; }
</style>
</head>
<body>
<main class="canvas">

  <section class="card card--front" aria-label="Card front">
    <svg class="front-band" viewBox="0 0 640 380" preserveAspectRatio="none" aria-hidden="true">
      <polygon points="0,108 640,128 640,298 0,250" fill="#ffffff"/>
    </svg>
    <p class="company-name"><span class="company-name__square" aria-hidden="true"></span><span>Bramwell's Mobile Transport</span></p>
    <div class="truck-art" role="img" aria-label="Illustration of a green and white truck hauling a mobile home"></div>
    <p class="web">www.bramwellmtransport.com</p>
  </section>

  <section class="card card--back" aria-label="Card back">
    <p class="company-name"><span class="company-name__square" aria-hidden="true"></span><span>Bramwell's Mobile Transport</span></p>
    <div class="truck-art" role="img" aria-label="Illustration of a green and white truck hauling a mobile home"></div>
    <div class="services-bar">
      <span>HERE SERVICES&nbsp;&nbsp;|</span>
      <span>SERVICES&nbsp;&nbsp;|</span>
    </div>
    <div class="contact-panel">
      <p class="person">
        <span class="person__name">NAME BRAMWELL</span>
        <span class="person__role">DIRECTOR</span>
      </p>
      <p class="contacts">CONTACTS</p>
    </div>
  </section>

</main>
</body>
</html>
```